Covid19 Poster for workplaces

Create a poster on how to protect yourself from Corona virus at work.
We are a Teamwell Works company. We have just re-branded so we need to fit in with our brand. We like clean and fresh, slightly amusing is ok if it will draw attention but it's an important topic. A4 and A3 please.

Content:

Headline: Lower the risk of COVID 19 in the workplace.

BE WELL

Bring your own cup - don’t share cups and food.
Elbow tap instead of handshakes and kisses
Wash your hands often - with soap.
Elbow or tissues when you cough or sneeze then straight in the bin
Leave your face alone after touching shared surfaces
Leave your bugs at home if you’re feeling unwell.

Call health line if you have a cough, a high temperature and shortness of breath. 0800 472 9160

Based on recommendations from ZPK and QLN

Target Market(s)

Employees - so anyone

Other font styles liked:
• Use the closest font to the brand documents

Requirements
Should not have
• Clip art

```html
<!DOCTYPE html>
<html lang="en">
<head>
<meta charset="utf-8">
<title>Lower the risk of COVID 19 in the workplace</title>
<link rel="stylesheet" href="https://fonts.googleapis.com/css2?family=Montserrat:wght@500;600;700;800;900&display=swap">
<style>
  :root {
    --teal: #1bb3c2;
    --teal-dark: #1398a6;
    --lime: #d8ef3a;
    --red: #c8102e;
    --navy: #24306b;
    --ink: #1c2340;
    --white: #ffffff;
    --virus-pink: #f3c9cf;
    --virus-blue: #5a6fc4;
  }
  * { box-sizing: border-box; margin: 0; padding: 0; }
  html, body { width: 849px; height: 1200px; overflow: hidden; background: var(--white); }
  .poster {
    position: relative;
    width: 849px;
    height: 1200px;
    overflow: hidden;
    background: var(--white);
    font-family: "Montserrat", Arial, sans-serif;
    color: var(--ink);
  }
  .brand {
    position: absolute;
    left: 34px;
    top: 22px;
    display: flex;
    align-items: center;
    gap: 10px;
    z-index: 3;
  }
  .brand-mark {
    width: 26px; height: 26px;
    border-radius: 50%;
    background: var(--teal);
  }
  .brand-name {
    font-weight: 700;
    font-size: 21px;
    line-height: 1.05;
    color: var(--teal);
  }
  .header-band {
    position: absolute;
    left: 0; top: 80px;
    width: 849px; height: 160px;
    background: var(--teal);
    z-index: 1;
  }
  .hero-visual {
    position: absolute;
    right: 0; top: 0;
    width: 430px; height: 210px;
    background: radial-gradient(circle at 40% 45%, #8fa0e6 0%, var(--virus-blue) 45%, #3a4aa0 100%);
    border-bottom-left-radius: 40px;
    z-index: 2;
  }
  .headline {
    position: absolute;
    left: 34px; top: 92px;
    z-index: 3;
    font-weight: 900;
    text-transform: uppercase;
    line-height: 1;
  }
  .headline .lead { display: block; color: var(--lime); font-size: 36px; letter-spacing: 0.5px; }
  .headline .subject {
    display: flex; align-items: center;
    color: var(--white); font-size: 66px; margin: 6px 0 4px; letter-spacing: 1px;
  }
  .headline .subject .virus-o {
    display: inline-block; width: 54px; height: 54px; border-radius: 50%;
    background: var(--red); margin: 0 3px; box-shadow: 0 0 0 5px rgba(200,16,46,0.35);
  }
  .headline .subject .num { margin-left: 18px; }
  .headline .tail { display: block; color: var(--white); font-size: 36px; }
  .body-visual {
    position: absolute;
    right: 0; top: 240px;
    width: 520px; height: 800px;
    background: radial-gradient(ellipse at 75% 35%, var(--virus-pink) 0%, #f9e3e6 35%, rgba(255,255,255,0) 70%);
    z-index: 0;
  }
  .tips {
    position: absolute;
    left: 80px; top: 272px;
    width: 720px;
    list-style: none;
    z-index: 2;
  }
  .tips li {
    display: flex;
    align-items: flex-start;
    gap: 22px;
    font-weight: 600;
    font-size: 30px;
    line-height: 1.18;
    margin-bottom: 24px;
  }
  .tips .bullet { flex: 0 0 auto; width: 34px; height: 34px; margin-top: 2px; }
  .helpline {
    position: absolute;
    left: 0; top: 1040px;
    width: 849px; height: 66px;
    background: var(--teal);
    display: flex; align-items: center; justify-content: center; gap: 14px;
    color: var(--white);
    font-weight: 700;
    font-size: 38px;
    letter-spacing: 0.5px;
  }
  .helpline svg { width: 34px; height: 34px; }
  .source {
    position: absolute;
    left: 0; top: 1128px;
    width: 849px;
    text-align: center;
    color: var(--navy);
    font-weight: 700;
    font-size: 27px;
  }
</style>
</head>
<body>
<main class="poster">
  <div class="brand">
    <span class="brand-mark"></span>
    <span class="brand-name">Teamwell<br>Works</span>
  </div>

  <div class="hero-visual" role="img" aria-label="Heart shapes filled with magnified virus particles"></div>
  <div class="header-band"></div>

  <h1 class="headline">
    <span class="lead">Lower the risk of</span>
    <span class="subject">C<span class="virus-o"></span>VID<span class="num">19</span></span>
    <span class="tail">In the workplace</span>
  </h1>

  <div class="body-visual" role="img" aria-label="Soft background of pink and red virus particles"></div>

  <ul class="tips">
    <li><svg class="bullet" viewBox="0 0 34 34"><circle cx="17" cy="17" r="13" fill="var(--red)"/></svg>Bring your own cup</li>
    <li><svg class="bullet" viewBox="0 0 34 34"><circle cx="17" cy="17" r="13" fill="var(--red)"/></svg>don't share cups and food</li>
    <li><svg class="bullet" viewBox="0 0 34 34"><circle cx="17" cy="17" r="13" fill="var(--red)"/></svg>Elbow tap instead of handshakes and kisses</li>
    <li><svg class="bullet" viewBox="0 0 34 34"><circle cx="17" cy="17" r="13" fill="var(--red)"/></svg>Wash your hands often - with soap</li>
    <li><svg class="bullet" viewBox="0 0 34 34"><circle cx="17" cy="17" r="13" fill="var(--red)"/></svg>Elbow or tissues when you cough or sneeze then straight in the bin</li>
    <li><svg class="bullet" viewBox="0 0 34 34"><circle cx="17" cy="17" r="13" fill="var(--red)"/></svg>Leave your face alone after touching shared surfaces</li>
    <li><svg class="bullet" viewBox="0 0 34 34"><circle cx="17" cy="17" r="13" fill="var(--red)"/></svg>Leave your bugs at home if you're feeling unwell</li>
    <li><svg class="bullet" viewBox="0 0 34 34"><circle cx="17" cy="17" r="13" fill="var(--red)"/></svg>Call health line if you have a cough a high temperature and shortness of breath</li>
  </ul>

  <div class="helpline">
    <svg viewBox="0 0 24 24" aria-hidden="true"><path fill="var(--white)" d="M6.6 10.8a15.1 15.1 0 0 0 6.6 6.6l2.2-2.2a1 1 0 0 1 1-.25 11.4 11.4 0 0 0 3.6.57 1 1 0 0 1 1 1V20a1 1 0 0 1-1 1A17 17 0 0 1 3 4a1 1 0 0 1 1-1h3.5a1 1 0 0 1 1 1c0 1.25.2 2.45.57 3.57a1 1 0 0 1-.25 1z"/></svg>
    <span>0800 472 9160</span>
  </div>

  <p class="source">Based on recommendations from ZPK and QLN</p>
</main>
</body>
</html>
```